Australian Trucking Company Requires Professional Looking Stationary

We require a professional looking stationary design that incorporates our newly designed logo.

Our business, called "Vell Haulage Contracting", provides contracting work, transport and logistics to business in Western Australia particularly with links to the mining sector.

We are a small business looking to expand and our new logo and our new stationary will help develop our brand image in our market place.

Target Market(s)

Businesses and Corporation with links to the Mining Sector

Industry/Entity Type

Small Business

Requirements
Must have
• The letterhead must have the following details:
The new logo

Text saying: "Vell Haulage Pty Ltd (ACN 582 306 917) ATF The Vell Discretionary Trust T/AS"
"ABN 71 840 239 568"
Address "P.O Box 817 Ashbury WA, 6912"
Phone: 08 9172 5840
Email: vellhaul@mailnest.com.au

The text on the letterhead should be editable as the details are likely to change in the near future. Provision should be made for a website address all though one isn't available at the moment.

The styling, layout and font text is entirely up to the designer.

```html
<!DOCTYPE html>
<html lang="en">
<head>
<meta charset="utf-8">
<title>Vell Haulage Contracting — Stationery Set</title>
<link rel="stylesheet" href="https://fonts.googleapis.com/css2?family=Open+Sans:wght@400;600;800&display=swap">
<style>
  :root {
    --red: #d71f27;
    --red-deep: #a3141b;
    --red-soft: #e8474d;
    --ink: #3a3a3a;
    --grey: #8a8a8a;
    --grey-light: #e4e4e4;
    --paper: #ffffff;
    --charcoal: #3d3d3d;
    --charcoal-deep: #262626;
    --canvas: #d9d9d9;
  }
  * { box-sizing: border-box; margin: 0; padding: 0; }
  html, body { width: 1200px; height: 872px; overflow: hidden; }
  body {
    position: relative;
    background: var(--canvas);
    font-family: "Open Sans", Arial, sans-serif;
    color: var(--ink);
  }
  .piece { position: absolute; overflow: hidden; background: var(--paper); }

  /* shared brand elements */
  .brand-name {
    display: flex; align-items: center; gap: 6px;
    font-weight: 800; text-transform: uppercase; line-height: 1.05;
    color: var(--red);
  }
  .brand-name .brand-dot { width: 8px; height: 8px; background: currentColor; flex: none; }
  .brand-name--light { color: var(--paper); }
  .top-band {
    position: absolute; left: 0; top: 0; right: 0;
    background: linear-gradient(90deg, var(--red-deep), var(--red) 60%, var(--red-soft));
  }
  .truck-art { position: absolute; border-radius: 6px; }
  .icon { display: inline-block; width: 7px; height: 7px; background: var(--red); margin: 0 3px 0 8px; vertical-align: middle; }
  .icon:first-child { margin-left: 0; }

  /* letterhead */
  .letterhead { left: 40px; top: 40px; width: 420px; height: 594px; }
  .letterhead .top-band { height: 18px; clip-path: polygon(35% 0, 100% 0, 100% 100%, 40% 100%); }
  .letterhead .brand-name { position: absolute; left: 34px; top: 40px; font-size: 17px; width: 150px; }
  .letterhead .truck-art {
    right: 20px; bottom: 70px; width: 150px; height: 120px;
    background: linear-gradient(135deg, #f2f2f2, #e3e3e3);
  }
  .letter-body { position: absolute; left: 60px; top: 130px; width: 300px; font-size: 7.5px; line-height: 1.55; }
  .recipient { margin-bottom: 12px; }
  .salutation { margin-bottom: 10px; }
  .letter-body p { margin-bottom: 9px; }
  .sign-off { margin-top: 16px; }
  .signature {
    width: 60px; height: 20px; margin: 6px 0;
    background: linear-gradient(90deg, #cfcfcf, #e6e6e6); border-radius: 3px;
  }
  .letter-footer {
    position: absolute; left: 34px; right: 34px; bottom: 22px;
    border-top: 2px solid var(--red); padding-top: 6px;
    font-size: 6.6px; line-height: 1.6; color: var(--grey);
  }
  .letter-footer .abn { color: var(--red); font-weight: 600; }

  /* DL envelope front */
  .envelope-front { left: 490px; top: 40px; width: 380px; height: 190px; }
  .envelope-front .top-band { height: 20px; clip-path: polygon(30% 0, 100% 0, 100% 100%, 34% 100%); }
  .envelope-front .brand-name { position: absolute; left: 20px; top: 34px; font-size: 12px; width: 110px; }
  .envelope-window {
    position: absolute; left: 24px; top: 80px; width: 150px; height: 56px;
    border: 1px solid #cfcfcf; border-radius: 10px;
    background: linear-gradient(180deg, #f7f7f7, #e9e9e9);
  }
  .envelope-front .truck-art {
    right: 14px; top: 32px; width: 120px; height: 110px;
    background: linear-gradient(135deg, #f3f3f3, #e6e6e6);
  }
  .envelope-footer {
    position: absolute; left: 20px; right: 20px; bottom: 10px;
    font-size: 5.6px; line-height: 1.6; color: var(--grey);
  }

  /* envelope back */
  .envelope-back { left: 490px; top: 250px; width: 380px; height: 190px; }
  .envelope-back .flap { position: absolute; inset: 0; }
  .envelope-back .brand-name { position: absolute; left: 150px; top: 24px; font-size: 11px; width: 100px; }

  /* presentation folder */
  .folder {
    left: 900px; top: 40px; width: 260px; height: 368px;
    background: linear-gradient(160deg, var(--red-soft), var(--red) 45%, var(--red-deep));
  }
  .folder .brand-name { position: absolute; left: 24px; top: 60px; font-size: 20px; width: 170px; }
  .folder .truck-art {
    right: 0; bottom: 30px; width: 170px; height: 150px;
    background: linear-gradient(135deg, rgba(255,255,255,0.12), rgba(120,0,0,0.25));
  }

  /* business cards */
  .card { width: 180px; height: 110px; border-radius: 10px; }
  .card-front { left: 490px; top: 470px; }
  .card-front .top-band { height: 12px; clip-path: polygon(30% 0, 100% 0, 100% 100%, 36% 100%); }
  .card-front .brand-name { position: absolute; left: 12px; top: 19px; font-size: 9px; width: 100px; gap: 5px; }
  .card-front .brand-name .brand-dot { width: 6px; height: 6px; }
  .card-front .person { position: absolute; left: 12px; top: 43px; }
  .person-name { color: var(--red); font-size: 10px; font-weight: 600; line-height: 1.3; }
  .person-role { color: var(--grey); font-size: 6.5px; line-height: 1.3; }
  .card-contact {
    position: absolute; left: 12px; bottom: 7px; font-size: 4.8px; line-height: 1.5; color: var(--grey);
  }
  .card-front .truck-art {
    right: 8px; top: 18px; width: 56px; height: 46px;
    background: linear-gradient(135deg, #f3f3f3, #e4e4e4);
  }
  .card-red {
    left: 690px; top: 470px;
    background: linear-gradient(150deg, var(--red-soft), var(--red) 50%, var(--red-deep));
  }
  .card-red .brand-name, .card-dark .brand-name { position: absolute; left: 60px; top: 34px; font-size: 12px; width: 110px; }
  .card-red .truck-art {
    left: 10px; top: 16px; width: 44px; height: 78px;
    background: linear-gradient(135deg, rgba(255,255,255,0.15), rgba(120,0,0,0.25));
  }
  .card-dark {
    left: 490px; top: 600px;
    background: linear-gradient(150deg, var(--charcoal), var(--charcoal-deep));
  }
</style>
</head>
<body>

<!-- Letterhead -->
<section class="piece letterhead" aria-label="Letterhead">
  <div class="top-band"></div>
  <div class="brand-name"><span class="brand-dot"></span><span>Vell Haulage Contracting</span></div>
  <div class="truck-art" role="img" aria-label="Faint truck illustration watermark"></div>
  <div class="letter-body">
    <div class="recipient">Name<br>Title<br>Company Name<br>Address<br>City, State, Zip Code</div>
    <div class="salutation">Dear Nora Beck,</div>
    <p>Thank you for your recent enquiry about our haulage services. We are pleased to confirm that our fleet is available for the coming season and can support your site with bulk transport, equipment moves and contract crews across the region.</p>
    <p>Please find our schedule of rates attached. Our team will contact you this week to arrange a site visit and discuss timing, access and safety requirements in detail.</p>
    <div class="sign-off">Sincerely,</div>
    <div class="signature" role="img" aria-label="Handwritten signature"></div>
    <div>Your Name goes here<br>Consultant Manager</div>
  </div>
  <footer class="letter-footer">
    <div>Vell Haulage Pty Ltd (ACN 582 306 917) ATF The Vell Discretionary Trust T/AS</div>
    <div><span class="abn">ABN</span> 71 840 239 568 <span class="icon"></span>P.O Box 817 Ashbury WA, 6912 <span class="icon"></span>08 9172 5840 <span class="icon"></span>vellhaul@mailnest.com.au</div>
  </footer>
</section>

<!-- DL window envelope -->
<section class="piece envelope-front" aria-label="Window envelope front">
  <div class="top-band"></div>
  <div class="brand-name"><span class="brand-dot"></span><span>Vell Haulage Contracting</span></div>
  <div class="envelope-window"></div>
  <div class="truck-art" role="img" aria-label="Faint truck illustration watermark"></div>
  <div class="envelope-footer">
    <div>Vell Haulage Pty Ltd (ACN 582 306 917) ATF The Vell Discretionary Trust T/AS</div>
    <div><span class="icon"></span>ABN 71 840 239 568 <span class="icon"></span>P.O Box 817 Ashbury WA, 6912 <span class="icon"></span>08 9172 5840 <span class="icon"></span>vellhaul@mailnest.com.au</div>
  </div>
</section>

<!-- Envelope back -->
<section class="piece envelope-back" aria-label="Envelope back">
  <svg class="flap" viewBox="0 0 380 190" preserveAspectRatio="none" aria-hidden="true">
    <defs>
      <linearGradient id="flapRed" x1="0" y1="0" x2="1" y2="1">
        <stop offset="0" stop-color="#e8474d"/>
        <stop offset="1" stop-color="#a3141b"/>
      </linearGradient>
    </defs>
    <path d="M0 0 H380 V10 L210 70 Q190 78 170 70 L0 10 Z" fill="url(#flapRed)"/>
    <path d="M0 10 L170 70 Q190 78 210 70 L380 10" fill="none" stroke="#dddddd" stroke-width="1"/>
  </svg>
  <div class="brand-name brand-name--light"><span class="brand-dot"></span><span>Vell Haulage Contracting</span></div>
</section>

<!-- Presentation folder -->
<section class="piece folder" aria-label="Presentation folder">
  <div class="brand-name brand-name--light"><span class="brand-dot"></span><span>Vell Haulage Contracting</span></div>
  <div class="truck-art" role="img" aria-label="Large tonal truck illustration"></div>
</section>

<!-- Business card, front -->
<section class="piece card card-front" aria-label="Business card front">
  <div class="top-band"></div>
  <div class="brand-name"><span class="brand-dot"></span><span>Vell Haulage<br>Contracting</span></div>
  <div class="truck-art" role="img" aria-label="Faint truck illustration watermark"></div>
  <div class="person">
    <div class="person-name">Lewis Harlow</div>
    <div class="person-role">President</div>
  </div>
  <div class="card-contact">
    <div>Vell Haulage Pty Ltd (ACN 582 306 917)</div>
    <div>ABN 71 840 239 568</div>
    <div>P.O Box 817 Ashbury WA, 6912</div>
    <div>08 9172 5840 · vellhaul@mailnest.com.au</div>
  </div>
</section>

<!-- Business card, red reverse -->
<section class="piece card card-red" aria-label="Business card reverse, red">
  <div class="truck-art" role="img" aria-label="Tonal truck illustration"></div>
  <div class="brand-name brand-name--light"><span class="brand-dot"></span><span>Vell Haulage Contracting</span></div>
</section>

<!-- Business card, charcoal reverse -->
<section class="piece card card-dark" aria-label="Business card reverse, charcoal">
  <div class="brand-name brand-name--light"><span class="brand-dot"></span><span>Vell Haulage Contracting</span></div>
</section>

</body>
</html>
```